Brook Medical Needs a PowerPoint Design

Brook Medical needs a PowerPoint template developed for use during presentations by our marketing department. Brook offers Medical specialty services to family physicians throughout Calgary. At Brook we pride ourselves on our commitment to our patients as well as having very short wait times and convenient locations spread throughout the communities. We offer services in Pulmonary Diagnostics as well as sleep apnea assessment and treatment. Consults from medical specialties such as Respirology, Physiatry, Internal Medicine, Occupational Medicine, Pediatric Infectious Disease, and alergy are also available.

***Please note we are not looking for you to build a presentation we just want the design of the slides for us to add content as needed****

We require an updated powerpoint template that we can use in a range of situations such as during marketing presentations or professional educational events. We would like a design that is modern and unique. We would like the mountain theme built into the design elements of the slide deck

We require a whole slide deck (Title slide; etc) for the Brook Medical Group as well as a body slide for our sleep division.

Our usual font is ArnoPro Semi Bold

Our Websites: brookairway.example brookrestclinic.example

Closest pantone color for Brook’s purple is PMS 814 2X

Target Market(s)

Physicians, medical professionals

Industry/Entity Type

Medical

Font styles to use
Other font styles liked:
• ArnoPro Semi Bold

Requirements
Must have
• Similar look and feel to sleep and medical slide
Nice to have
• Mountain design built into deck.
Should not have
• large actual images of mountains.

```html
<!DOCTYPE html>
<html lang="en">
<head>
<meta charset="utf-8">
<title>Brook Medical – Slide Deck Template</title>
<link rel="stylesheet" href="https://fonts.googleapis.com/css2?family=Roboto:wght@400;500;700&display=swap">
<style>
  :root {
    --purple: #5b3a96;
    --purple-dark: #4a2d80;
    --purple-soft: #7a5db0;
    --ink: #3a3a3a;
    --muted: #8a8a8a;
    --grey-box: #e4e4e4;
    --page: #ffffff;
    --line: #d9d4e6;
  }
  * { box-sizing: border-box; margin: 0; padding: 0; }
  html, body { width: 814px; height: 1200px; overflow: hidden; background: var(--page); }
  body { font-family: "Roboto", Arial, sans-serif; color: var(--ink); }

  .deck {
    display: grid;
    grid-template-columns: 390px 390px;
    grid-template-rows: repeat(4, 288px);
    gap: 8px 10px;
    padding: 8px 12px;
  }
  .slide {
    position: relative;
    background: #fff;
    border: 1px solid #e2e2e2;
    overflow: hidden;
  }

  /* shared pieces */
  .brand { display: flex; align-items: center; gap: 5px; color: var(--purple); font-weight: 500; }
  .brand-dot { width: 9px; height: 9px; border-radius: 50%; background: var(--purple); }
  .brand-name { font-size: 12px; letter-spacing: .3px; line-height: 1; }
  .brand.light { color: #fff; }
  .brand.light .brand-dot { background: #fff; }

  .slide-header {
    position: absolute; left: 0; right: 0; top: 0; height: 24px;
    background: var(--purple);
    display: flex; align-items: center; justify-content: space-between;
    padding: 0 10px;
  }
  .slide-header h2 { color: #fff; font-size: 12px; font-weight: 500; letter-spacing: .3px; }
  .slide-header .brand-name { font-size: 9px; }
  .slide-header .brand-dot { width: 7px; height: 7px; }

  .slide-footer {
    position: absolute; left: 0; right: 0; bottom: 0; height: 11px;
    background: var(--purple-dark);
    display: flex; align-items: center; justify-content: space-between;
    padding: 0 8px; color: #fff; font-size: 5px;
  }

  .subtitle { color: var(--purple); font-size: 8px; font-weight: 700; margin-bottom: 5px; }
  .body-text { font-size: 4.6px; line-height: 1.45; color: var(--muted); margin-bottom: 6px; }

  /* title slide */
  .title-band {
    position: absolute; left: 0; right: 0; top: 0; height: 140px;
    background: linear-gradient(135deg, var(--purple-soft), var(--purple));
    padding: 14px 0 0 142px; color: #fff;
  }
  .title-band h1 { font-size: 16px; font-weight: 500; margin-bottom: 6px; }
  .title-band p { font-size: 5px; line-height: 1.5; opacity: .9; max-width: 170px; }
  .title-brand { position: absolute; left: 142px; top: 188px; }
  .title-brand .brand-name { font-size: 15px; }
  .title-brand .brand-dot { width: 14px; height: 14px; }

  /* photo title slide */
  .photo-band {
    position: absolute; left: 0; right: 0; top: 0; height: 148px;
    background: linear-gradient(180deg, #8fb4d8 0%, #c9dbea 55%, #7d8a96 100%);
  }
  .photo-title { position: absolute; left: 42px; top: 162px; }
  .photo-title h1 { color: var(--purple); font-size: 13px; font-weight: 500; margin-bottom: 5px; }
  .photo-title p { font-size: 4.6px; line-height: 1.5; color: var(--muted); max-width: 160px; }
  .photo-brand { position: absolute; right: 26px; top: 172px; }

  /* content slides */
  .content { position: absolute; top: 36px; left: 24px; right: 24px; bottom: 20px; }
  .cols { display: grid; grid-template-columns: 1fr 1fr; gap: 18px; }
  .grey-box { background: var(--grey-box); }

  .portrait {
    background: linear-gradient(180deg, #d5d9e0, #6b7585);
  }
  .caption { font-size: 5.5px; color: var(--purple); font-weight: 700; letter-spacing: .3px; }
  .caption span { font-weight: 400; }

  .bio-box { background: var(--purple); color: #fff; padding: 8px; }
  .bio-box h3 { font-size: 6px; font-weight: 500; margin-bottom: 4px; }
  .bio-box p { font-size: 4.4px; line-height: 1.5; opacity: .9; }

  .bullet-row { display: flex; gap: 6px; align-items: flex-start; }
  .bullet-ring { width: 8px; height: 8px; border: 1px solid var(--purple); border-radius: 50%; flex: none; margin-top: 1px; }

  /* thank you slide */
  .thanks { background: linear-gradient(135deg, var(--purple-soft), var(--purple-dark)); color: #fff; }
  .thanks-brand { position: absolute; left: 34px; top: 118px; }
  .thanks-brand .brand-name { font-size: 13px; }
  .thanks-panel { position: absolute; left: 196px; top: 30px; right: 20px; }
  .thanks-panel h2 { font-size: 15px; font-weight: 400; margin-bottom: 10px; }
  .thanks-panel p { font-size: 6px; line-height: 1.5; opacity: .9; margin-bottom: 14px; }
  .contact { list-style: none; font-size: 6px; }
  .contact li { display: flex; align-items: center; gap: 6px; margin-bottom: 7px; }
  .contact svg { width: 8px; height: 8px; flex: none; }
</style>
</head>
<body>
<main class="deck">

  <!-- Title slide -->
  <section class="slide">
    <div class="title-band">
      <h1>Project Title Here</h1>
      <p>Subtitle text goes right here, enter your short intro line and a second line of supporting detail.</p>
    </div>
    <div class="brand title-brand"><span class="brand-dot"></span><span class="brand-name">Brook Medical</span></div>
    <footer class="slide-footer"><span>Copyright text here</span><span>Page 1</span></footer>
  </section>

  <!-- Photo title slide -->
  <section class="slide">
    <div class="photo-band" role="img" aria-label="Wide photograph of snowy mountains under a blue sky"></div>
    <div class="photo-title">
      <h1>Project Title Here</h1>
      <p>Subtitle text goes right here, enter your short intro line and a second line of supporting detail.</p>
    </div>
    <div class="brand photo-brand"><span class="brand-dot"></span><span class="brand-name">Brook Medical</span></div>
    <footer class="slide-footer"><span>Copyright text here</span><span>Page 1</span></footer>
  </section>

  <!-- Text + boxes -->
  <section class="slide">
    <header class="slide-header"><h2>PROJECT TITLE HERE</h2><div class="brand light"><span class="brand-dot"></span><span class="brand-name">Brook Medical</span></div></header>
    <div class="content cols">
      <div>
        <h3 class="subtitle">Subtitle Title Here</h3>
        <p class="body-text">Subtitle text here, add your own content to this area and keep lines short and clear.</p>
        <p class="body-text">Subtitle text here, add your own content to this area and keep lines short and clear for readers.</p>
        <p class="body-text">Subtitle text here, add your own content to this area and keep lines short.</p>
        <p class="body-text">Subtitle text here, add your own content to this area.</p>
      </div>
      <div style="display:grid;grid-template-rows:1fr 1fr;gap:14px;padding-bottom:14px;">
        <div class="grey-box"></div>
        <div class="grey-box"></div>
      </div>
    </div>
    <footer class="slide-footer"><span>Copyright text here</span><span>Page 1</span></footer>
  </section>

  <!-- Blank -->
  <section class="slide">
    <header class="slide-header"><h2>PROJECT TITLE HERE</h2><div class="brand light"><span class="brand-dot"></span><span class="brand-name">Brook Medical</span></div></header>
    <footer class="slide-footer"><span>Copyright text here</span><span>Page 1</span></footer>
  </section>

  <!-- Two columns -->
  <section class="slide">
    <header class="slide-header"><h2>PROJECT TITLE HERE</h2><div class="brand light"><span class="brand-dot"></span><span class="brand-name">Brook Medical</span></div></header>
    <div class="content cols">
      <div>
        <h3 class="subtitle">Subtitle Title Here</h3>
        <p class="body-text">Subtitle text here, add your own content to this area and keep lines short and clear.</p>
        <p class="body-text">Subtitle text here, add your own content to this area and keep lines short and clear.</p>
        <p class="body-text">Subtitle text here, add your own content to this area and keep lines short.</p>
        <p class="body-text">Subtitle text here, add your own content to this area.</p>
      </div>
      <div>
        <h3 class="subtitle">Subtitle Title Here</h3>
        <p class="body-text">Subtitle text here, add your own content to this area and keep lines short and clear.</p>
        <p class="body-text">Subtitle text here, add your own content to this area and keep lines short and clear.</p>
        <p class="body-text">Subtitle text here, add your own content to this area and keep lines short.</p>
        <p class="body-text">Subtitle text here, add your own content to this area.</p>
      </div>
    </div>
    <footer class="slide-footer"><span>Copyright text here</span><span>Page 1</span></footer>
  </section>

  <!-- Profile -->
  <section class="slide">
    <header class="slide-header"><h2>PROJECT TITLE HERE</h2><div class="brand light"><span class="brand-dot"></span><span class="brand-name">Brook Medical</span></div></header>
    <div class="content" style="left:18px;right:18px;">
      <div class="bullet-row">
        <span class="bullet-ring"></span>
        <div>
          <h3 class="subtitle" style="margin-bottom:2px;">Bullet Title Here</h3>
          <p class="body-text">Subtitle text here, add your own content to this area and keep lines short and clear for every reader.</p>
        </div>
      </div>
      <div style="display:grid;grid-template-columns:110px 1fr;gap:6px;height:170px;">
        <div style="display:flex;flex-direction:column;gap:4px;">
          <div class="portrait" style="flex:1;" role="img" aria-label="Portrait photograph of the director in a suit"></div>
          <p class="caption">DIRECTOR <span>name</span></p>
        </div>
        <div class="bio-box">
          <h3>Your BIO</h3>
          <p>Short biography text goes here. Describe background, training and focus areas in a few brief lines. Short biography text goes here. Describe background, training and focus areas in a few brief lines. Short biography text goes here. Describe background, training and focus areas.</p>
        </div>
      </div>
    </div>
    <footer class="slide-footer"><span>Copyright text here</span><span>Page 1</span></footer>
  </section>

  <!-- Profile alt -->
  <section class="slide">
    <header class="slide-header"><h2>PROJECT TITLE HERE</h2><div class="brand light"><span class="brand-dot"></span><span class="brand-name">Brook Medical</span></div></header>
    <div class="content" style="left:18px;right:18px;">
      <div class="bullet-row">
        <span class="bullet-ring"></span>
        <p class="body-text">Subtitle text here, add your own content to this area and keep lines short and clear for every reader.</p>
      </div>
      <div class="bio-box" style="display:grid;grid-template-columns:100px 1fr;gap:8px;height:170px;margin-top:6px;">
        <div style="display:flex;flex-direction:column;gap:4px;">
          <div class="portrait" style="flex:1;" role="img" aria-label="Portrait photograph of the director in a suit"></div>
          <p class="caption" style="color:#fff;">DIRECTOR <span>name</span></p>
        </div>
        <div>
          <h3>Your BIO</h3>
          <p>Short biography text goes here. Describe background, training and focus areas in a few brief lines. Short biography text goes here. Describe background, training and focus areas in a few brief lines.</p>
        </div>
      </div>
    </div>
    <footer class="slide-footer"><span>Copyright text here</span><span>Page 1</span></footer>
  </section>

  <!-- Thank you -->
  <section class="slide thanks">
    <div class="brand light thanks-brand"><span class="brand-dot"></span><span class="brand-name">Brook Medical</span></div>
    <div class="thanks-panel">
      <h2>Thanks for your Time</h2>
      <p>Closing text goes here, add a short<br>line of thanks and a call to action<br>for your audience.</p>
      <ul class="contact">
        <li><svg viewBox="0 0 10 10"><path d="M2 1h2l1 2-1.2 1a5 5 0 0 0 2.2 2.2L7 5l2 1v2a1 1 0 0 1-1 1A7 7 0 0 1 1 2a1 1 0 0 1 1-1z" fill="#fff"/></svg>+1 000 555 0142</li>
        <li><svg viewBox="0 0 10 10"><rect x="1" y="2" width="8" height="6" fill="none" stroke="#fff"/><path d="M1 2l4 3 4-3" fill="none" stroke="#fff"/></svg>hello@brookairway.example</li>
        <li><svg viewBox="0 0 10 10"><circle cx="5" cy="5" r="4" fill="none" stroke="#fff"/><path d="M1 5h8M5 1c2 2 2 6 0 8M5 1c-2 2-2 6 0 8" fill="none" stroke="#fff" stroke-width=".7"/></svg>brookairway.example</li>
      </ul>
    </div>
  </section>

</main>
</body>
</html>
```